Security based company delivering High Risk Training to Law Enforcement Agencies Worldwide.

We need a Web design for a company doing business in Washington D.C. We deliver High Risk Training to Law Enforcement Agencies throughout the world. Our focus is on Improvised Explosive Devices. We train Bomb Technicians and First Responders in all aspects relating to bombings and criminal incidents globally.

Reason: We have uploaded our logo. Thank you.

Target Market(s)

Vanguard and Law Enforcement Personnel from around the world.

Industry/Entity Type

Business

Requirements
Should not have
• Do not include cartoon like characters.

```html
<!DOCTYPE html>
<html lang="en">
<head>
<meta charset="utf-8">
<title>Vanguard — High Risk Training</title>
<link rel="stylesheet" href="https://fonts.googleapis.com/css2?family=Open+Sans:wght@400;600;700&display=swap">
<style>
  :root {
    --page-dark: #2e2e2e;
    --nav-dark: #262626;
    --section-light: #ebebeb;
    --accent: #e84c3d;
    --text-light: #ffffff;
    --text-muted: #a9a9a9;
    --text-body: #9a9a9a;
    --heading-dark: #2b2b2b;
    --button-light: #f2f2f2;
  }
  * { margin: 0; padding: 0; box-sizing: border-box; }
  html, body { width: 903px; height: 1200px; overflow: hidden; }
  body {
    background: var(--page-dark);
    font-family: "Open Sans", Arial, sans-serif;
    color: var(--text-light);
    position: relative;
  }

  .site-header {
    position: absolute; left: 0; top: 0; width: 903px; height: 55px;
    background: var(--nav-dark);
  }
  .brand {
    position: absolute; left: 60px; top: 14px;
    font-size: 22px; font-weight: 700; color: var(--text-light);
    letter-spacing: 0.2px;
  }
  .main-nav { position: absolute; right: 60px; top: 0; display: flex; height: 55px; }
  .main-nav a {
    display: block; padding: 0 16px; line-height: 55px;
    font-size: 9px; font-weight: 600; color: var(--text-muted);
    text-decoration: none; letter-spacing: 0.4px; position: relative;
  }
  .main-nav a.is-active { color: var(--text-light); }
  .main-nav a.is-active::after {
    content: ""; position: absolute; left: 12px; right: 12px; bottom: 12px;
    height: 2px; background: var(--accent);
  }

  .hero-band { position: absolute; left: 0; top: 55px; width: 903px; height: 353px; background: var(--page-dark); }
  .hero-slide {
    position: absolute; left: 60px; top: 0; width: 786px; height: 353px;
    background:
      radial-gradient(ellipse 150px 200px at 430px 200px, #6e5a4c 0%, #43372f 45%, rgba(30,28,26,0) 100%),
      linear-gradient(90deg, #151515 0%, #2b2826 40%, #2b2826 65%, #161616 100%);
  }
  .hero-title {
    position: absolute; left: 0; right: 0; top: 108px; text-align: center;
    font-size: 26px; font-weight: 700; color: var(--text-light); padding-left: 40px;
  }
  .hero-text {
    position: absolute; left: 0; right: 0; top: 180px; text-align: center;
    font-size: 11px; color: #dddddd;
  }
  .hero-actions { position: absolute; left: 164px; top: 220px; display: flex; gap: 14px; }
  .btn-light {
    display: inline-block; background: var(--button-light); color: #333;
    font-size: 9px; font-weight: 600; text-align: center; letter-spacing: 0.3px;
    text-decoration: none;
  }
  .hero-actions .btn-light { width: 123px; height: 37px; line-height: 37px; }
  .slider-arrow {
    position: absolute; top: 143px; width: 37px; height: 37px;
    border: 1px solid #d8d8d8;
  }
  .slider-arrow svg { position: absolute; left: 12px; top: 11px; }
  .slider-arrow.prev { left: 17px; }
  .slider-arrow.next { right: 20px; }

  .intro {
    position: absolute; left: 0; top: 408px; width: 903px; height: 229px;
    background: var(--section-light);
  }
  .accent-rule { position: absolute; width: 41px; height: 2px; background: var(--accent); }
  .intro .accent-rule { left: 60px; top: 32px; }
  .intro-title {
    position: absolute; left: 60px; top: 55px;
    font-size: 15px; font-weight: 600; color: var(--heading-dark);
  }
  .intro-title em { font-style: normal; color: var(--accent); }
  .intro-text {
    position: absolute; left: 60px; top: 91px; width: 780px;
    font-size: 10px; line-height: 17px; color: var(--text-body);
  }
  .btn-accent {
    position: absolute; left: 60px; top: 142px; width: 124px; height: 39px;
    line-height: 39px; text-align: center; background: var(--accent);
    color: var(--text-light); font-size: 9px; font-weight: 700; text-decoration: none;
  }

  .services-banner {
    position: absolute; left: 0; top: 637px; width: 903px; height: 138px;
    background: linear-gradient(90deg, #4a3a34 0%, #6e5244 30%, #a47a5c 55%, #d29b73 72%, #8e6a56 100%);
  }
  .services-banner .accent-rule { left: 60px; top: 18px; }
  .services-title {
    position: absolute; left: 60px; top: 40px;
    font-size: 36px; font-weight: 700; color: var(--text-light); line-height: 1;
  }
  .services-sub { position: absolute; left: 60px; top: 96px; font-size: 9px; color: var(--accent); }

  .features { position: absolute; left: 0; top: 775px; width: 903px; height: 425px; background: var(--page-dark); }
  .feature { position: absolute; top: 28px; width: 242px; }
  .feature:nth-child(1) { left: 70px; }
  .feature:nth-child(2) { left: 332px; }
  .feature:nth-child(3) { left: 595px; }
  .feature-icon { position: absolute; left: 0; top: 0; }
  .feature-title { position: absolute; left: 55px; top: 6px; font-size: 17px; font-weight: 600; white-space: nowrap; }
  .feature-tag { position: absolute; left: 55px; top: 32px; font-size: 8px; color: var(--text-muted); white-space: nowrap; }
  .feature-photo { position: absolute; left: 0; top: 80px; width: 242px; height: 154px; }
  .feature:nth-child(1) .feature-photo { background: linear-gradient(135deg, #4d4a3c 0%, #6b6752 50%, #3a382e 100%); }
  .feature:nth-child(2) .feature-photo { background: linear-gradient(135deg, #7c8a88 0%, #6e6a4e 55%, #8a8c7a 100%); }
  .feature:nth-child(3) .feature-photo { background: linear-gradient(135deg, #b8b8a8 0%, #7a7658 55%, #9c9a84 100%); }
  .feature-text { position: absolute; left: 0; top: 252px; width: 240px; font-size: 9.5px; line-height: 13px; color: #d0d0d0; }
  .feature .btn-light { position: absolute; left: 0; top: 305px; width: 99px; height: 29px; line-height: 29px; font-size: 8px; }
</style>
</head>
<body>
  <header class="site-header">
    <div class="brand">Vanguard</div>
    <nav class="main-nav">
      <a href="#" class="is-active">HOME</a>
      <a href="#">PAGES</a>
      <a href="#">LEFT SIDEBAR</a>
      <a href="#">RIGHT SIDEBAR</a>
      <a href="#">FULL PAGE</a>
      <a href="#">CONTACT US</a>
    </nav>
  </header>

  <section class="hero-band">
    <div class="hero-slide" role="img" aria-label="Photo of a soldier in camouflage face paint">
      <h1 class="hero-title">aliquam odio tortor, varius vel ipsum in</h1>
      <p class="hero-text">Mauris aliquam nulla et convallis adipiscing. Aenean tincidunt euismod</p>
      <div class="hero-actions">
        <a href="#" class="btn-light">GET STARTED</a>
        <a href="#" class="btn-light">READ MORE</a>
      </div>
      <div class="slider-arrow prev"><svg width="12" height="14" viewBox="0 0 12 14"><path d="M9 1 L3 7 L9 13" fill="none" stroke="#fff" stroke-width="1.5"/></svg></div>
      <div class="slider-arrow next"><svg width="12" height="14" viewBox="0 0 12 14"><path d="M3 1 L9 7 L3 13" fill="none" stroke="#fff" stroke-width="1.5"/></svg></div>
    </div>
  </section>

  <section class="intro">
    <div class="accent-rule"></div>
    <h2 class="intro-title">Donec at mattis lectus, <em>adipiscing pretium</em> ligula.</h2>
    <p class="intro-text">Phasellus laoreet massa id justo mattis pharetra. Fusce suscipit ligula vel quam viverra sit amet mollis tortor congue. Sed quis mauris sit amet magna accumsan tristique.</p>
    <a href="#" class="btn-accent">MORE INFO</a>
  </section>

  <section class="services-banner" role="img" aria-label="Photo of soldiers silhouetted against a sunset with a tank">
    <div class="accent-rule"></div>
    <h2 class="services-title">services</h2>
    <p class="services-sub">Suspendisse ultrices nulla</p>
  </section>

  <section class="features">
    <article class="feature">
      <svg class="feature-icon" width="44" height="48" viewBox="0 0 44 48">
        <polygon points="22,0 44,12 44,36 22,48 0,36 0,12" fill="var(--accent)"/>
        <polygon points="22,13 25,21 33,21 27,26 29,34 22,29 15,34 17,26 11,21 19,21" fill="none" stroke="#fff" stroke-width="1.6" stroke-linejoin="round"/>
      </svg>
      <h3 class="feature-title">Modern Design</h3>
      <p class="feature-tag">Maecenas fermentum semper</p>
      <div class="feature-photo" role="img" aria-label="Photo of soldiers standing in formation"></div>
      <p class="feature-text">Lorem ipsum dolor sit amet, consectetuer adipiscing elit. Donec odio. Quisque volutpat mattis eros.</p>
      <a href="#" class="btn-light">LEARN MORE</a>
    </article>
    <article class="feature">
      <svg class="feature-icon" width="44" height="48" viewBox="0 0 44 48">
        <polygon points="22,0 44,12 44,36 22,48 0,36 0,12" fill="var(--accent)"/>
        <path d="M22 12 C28 19 31 23 31 28 C31 33 27 36 22 36 C17 36 13 33 13 28 C13 24 16 21 18 19 C18 23 20 25 22 25 C21 20 22 16 22 12 Z" fill="none" stroke="#fff" stroke-width="1.6" stroke-linejoin="round"/>
      </svg>
      <h3 class="feature-title">High Quality</h3>
      <p class="feature-tag">Maecenas fermentum semper</p>
      <div class="feature-photo" role="img" aria-label="Photo of a sniper in a camouflage suit"></div>
      <p class="feature-text">Lorem ipsum dolor sit amet, consectetuer adipiscing elit. Donec odio. Quisque volutpat mattis eros.</p>
      <a href="#" class="btn-light">LEARN MORE</a>
    </article>
    <article class="feature">
      <svg class="feature-icon" width="44" height="48" viewBox="0 0 44 48">
        <polygon points="22,0 44,12 44,36 22,48 0,36 0,12" fill="var(--accent)"/>
        <path d="M22 34 L12 24 C9 21 10 16 14 15 C17 14 20 16 22 19 C24 16 27 14 30 15 C34 16 35 21 32 24 Z" fill="none" stroke="#fff" stroke-width="1.6" stroke-linejoin="round"/>
      </svg>
      <h3 class="feature-title">Quick Support</h3>
      <p class="feature-tag">Maecenas fermentum semper</p>
      <div class="feature-photo" role="img" aria-label="Photo of a soldier with binoculars in the field"></div>
      <p class="feature-text">Lorem ipsum dolor sit amet, consectetuer adipiscing elit. Donec odio. Quisque volutpat mattis eros.</p>
      <a href="#" class="btn-light">LEARN MORE</a>
    </article>
  </section>
</body>
</html>
```